Corporate Letterhead

Looking for a new corporate letterhead design. Our colors are orange and gray.

We'd like it if the below could be included somehow in the letterhead.                                       

Partnerships | Results | Quality

• Logo, Company Name, Address, Phone #, Fax #, Web address, Email address (optional), the phrase "A Service Disable Veteran Owned Small Business".

```html
<!DOCTYPE html>
<html lang="en">
<head>
<meta charset="utf-8">
<title>Vantora Systems, Inc — Letterhead</title>
<link rel="stylesheet" href="https://fonts.googleapis.com/css2?family=Michroma&family=Crimson+Text:ital@1&display=swap">
<style>
  :root {
    --orange: #f7941d;
    --orange-faint: #fdf1e2;
    --gray: #6d6e71;
    --gray-dark: #4d4d4f;
    --rule: #808285;
    --paper: #ffffff;
  }
  html, body {
    margin: 0;
    padding: 0;
    overflow: hidden;
    background: var(--paper);
  }
  .letterhead {
    position: relative;
    width: 927px;
    height: 1200px;
    overflow: hidden;
    background: var(--paper);
  }
  .brand {
    position: absolute;
    left: 82px;
    top: 58px;
    display: flex;
    align-items: center;
    gap: 22px;
  }
  .brand-dot {
    width: 72px;
    height: 72px;
    border-radius: 50%;
    background: var(--orange);
  }
  .brand-name {
    font-family: "Michroma", sans-serif;
    color: var(--orange);
    font-weight: 400;
    line-height: 1;
  }
  .brand-name .primary {
    display: block;
    font-size: 46px;
    letter-spacing: 2px;
  }
  .brand-name .secondary {
    display: block;
    font-size: 21px;
    margin-top: 10px;
    letter-spacing: 1px;
  }
  .contact {
    position: absolute;
    right: 80px;
    top: 66px;
    text-align: right;
    font-family: "Michroma", sans-serif;
    font-size: 17px;
    line-height: 22px;
    color: var(--gray);
    letter-spacing: 1px;
    margin: 0;
  }
  .contact .sep {
    display: inline-block;
    width: 8px;
    height: 8px;
    border-radius: 50%;
    background: var(--gray);
    vertical-align: middle;
    margin: 0 8px;
  }
  .header-rule {
    position: absolute;
    left: 68px;
    top: 168px;
    width: 788px;
    height: 3px;
    background: var(--rule);
  }
  .tagline {
    position: absolute;
    left: 0;
    width: 927px;
    top: 176px;
    text-align: center;
    font-family: "Michroma", sans-serif;
    font-style: italic;
    font-size: 15px;
    color: var(--gray);
    margin: 0;
  }
  .backdrop {
    position: absolute;
    left: 0;
    top: 0;
  }
  .values {
    position: absolute;
    top: 1090px;
    left: 0;
    width: 927px;
    display: flex;
    justify-content: center;
    align-items: center;
    font-family: "Crimson Text", serif;
    font-style: italic;
    font-size: 22px;
    color: var(--gray-dark);
  }
  .values .value { padding: 0 52px; }
  .values .divider {
    width: 3px;
    height: 40px;
    background: var(--gray-dark);
  }
</style>
</head>
<body>
<main class="letterhead">
  <svg class="backdrop" width="927" height="1200" aria-hidden="true">
    <circle cx="464" cy="627" r="350" fill="var(--orange-faint)"/>
  </svg>

  <header>
    <div class="brand">
      <span class="brand-dot"></span>
      <div class="brand-name">
        <span class="primary">VANTORA</span>
        <span class="secondary">SYSTEMS, INC</span>
      </div>
    </div>
    <p class="contact">
      STREET<br>
      CITY, STATE ZIP<br>
      PHONE<span class="sep"></span>FAX<br>
      WEB<span class="sep"></span>EMAIL
    </p>
    <div class="header-rule"></div>
    <p class="tagline">A Service Disable Veteran Owned Small Business</p>
  </header>

  <footer class="values">
    <span class="value">Partnerships</span>
    <span class="divider"></span>
    <span class="value">Results</span>
    <span class="divider"></span>
    <span class="value">Quality</span>
  </footer>
</main>
</body>
</html>
```